Vantage Sport And Fitness- Rates

I am opening up a new Gym/Training Facility. The Name of my New gym is Vantage Strength And Health. I am wanting to design a card that captures Membership Pricing/Personal Training Pricing. I will Upload the Logo. My colors are Red/Black/Silver. I really want there pricing card to "POP". IT needs to be very Professional and Clean. I will be placing these cards on a 5'7 . I would like these item on the card:
Name of Company: Vantage Strength And Health
Address:
2817 Larkmoor Commerce Dr.
Suite 214 Harlow, OH 43215
Phone #: 614-555-0187
website: www.vantagesh-example.com
Membership Rates:
$99/Month
$49 Heroes Rate
Family Plan:
2 People $149
3 People $199
4 People $299
Personal Training Rates:
1 session $102
5 sessions $490
10 sessions $940
20 sessions $1,800
40 sessions $3,400
Please be creative

```html
<!DOCTYPE html>
<html lang="en">
<head>
<meta charset="utf-8">
<title>Vantage Strength And Health – Rates Card</title>
<link rel="stylesheet" href="https://fonts.googleapis.com/css2?family=Montserrat:wght@600;700;800&family=Poppins:wght@400;500&display=swap">
<style>
  :root {
    --red: #e4202a;
    --black: #111111;
    --white: #ffffff;
    --stage: #d5d5d5;
    --text: #1c1c1c;
    --icon: #333333;
  }
  html, body {
    margin: 0;
    padding: 0;
    width: 1200px;
    height: 2250px;
    overflow: hidden;
    background: var(--stage);
  }
  .rates-card {
    position: absolute;
    left: 50px;
    top: 354px;
    width: 1100px;
    height: 1540px;
    box-shadow: 0 10px 30px rgba(0,0,0,0.18);
    background: var(--white);
  }
  .rates-card svg { display: block; }
  .brand-name { font-family: "Montserrat", sans-serif; font-weight: 700; font-size: 44px; fill: var(--red); }
  .headline { font-family: "Montserrat", sans-serif; font-weight: 800; fill: var(--black); }
  .headline--accent { fill: var(--red); }
  .rate-heading { font-family: "Poppins", sans-serif; font-weight: 500; font-size: 32px; fill: var(--red); }
  .rate-item { font-family: "Poppins", sans-serif; font-weight: 400; font-size: 28px; fill: var(--text); }
  .address { font-family: "Poppins", sans-serif; font-weight: 400; font-size: 25px; fill: var(--white); }
  .phone-number { font-family: "Montserrat", sans-serif; font-weight: 700; font-size: 62px; fill: var(--white); }
</style>
</head>
<body>
<div class="rates-card">
<svg width="1100" height="1540" viewBox="0 0 1100 1540" xmlns="http://www.w3.org/2000/svg">
  <defs>
    <linearGradient id="card-bg" x1="0" y1="0" x2="1" y2="1">
      <stop offset="0" stop-color="#ffffff"/>
      <stop offset="0.5" stop-color="#f1f1f2"/>
      <stop offset="1" stop-color="#ffffff"/>
    </linearGradient>
    <linearGradient id="hero-photo" x1="0" y1="0" x2="1" y2="1">
      <stop offset="0" stop-color="#2a2a2c"/>
      <stop offset="0.55" stop-color="#4a3a34"/>
      <stop offset="1" stop-color="#151515"/>
    </linearGradient>
    <linearGradient id="athlete-photo" x1="0" y1="0" x2="0" y2="1">
      <stop offset="0" stop-color="#f4f4f4"/>
      <stop offset="0.5" stop-color="#c9ab98"/>
      <stop offset="1" stop-color="#5a4a44"/>
    </linearGradient>
    <linearGradient id="gym-photo" x1="0" y1="0" x2="1" y2="1">
      <stop offset="0" stop-color="#6b6e74"/>
      <stop offset="1" stop-color="#2b2d33"/>
    </linearGradient>
  </defs>

  <rect class="card-background" width="1100" height="1540" fill="url(#card-bg)"/>

  <polyline class="chevron-line" points="0,91 255,350 589,0" fill="none" stroke="var(--red)" stroke-width="9"/>

  <g class="hero-photo" role="img" aria-label="Photo of two athletes lifting dumbbells">
    <polygon points="405,198 603,0 1100,0 1100,300 1060,345 590,345" fill="url(#hero-photo)" stroke="var(--red)" stroke-width="6"/>
  </g>

  <g class="gym-photo" role="img" aria-label="Photo of athlete training with a barbell">
    <polygon points="718,318 869,469 718,620 567,469" fill="url(#gym-photo)" stroke="var(--red)" stroke-width="6"/>
  </g>
  <g class="gym-photo" role="img" aria-label="Photo of a group fitness class">
    <polygon points="999,274 1100,375 1100,474 999,575 848,424" fill="url(#gym-photo)" stroke="var(--red)" stroke-width="6"/>
  </g>
  <g class="gym-photo" role="img" aria-label="Photo of people stretching in the gym">
    <polygon points="891,436 1042,587 891,738 740,587" fill="url(#gym-photo)" stroke="var(--red)" stroke-width="6"/>
  </g>

  <text class="brand-name" x="90" y="128">VANTAGE</text>

  <text class="headline" x="38" y="420" font-size="52">WELCOME TO</text>
  <text class="headline headline--accent" x="36" y="512" font-size="88">VANTAGE</text>
  <text class="headline" x="38" y="590" font-size="48">STRENGTH AND HEALTH</text>

  <g class="athlete-photo" role="img" aria-label="Photo of a woman lifting a dumbbell">
    <rect x="0" y="640" width="490" height="660" fill="url(#athlete-photo)"/>
  </g>

  <g class="rates">
    <g class="rate-icon" fill="none" stroke="var(--icon)" stroke-width="3">
      <rect x="537" y="758" width="40" height="30" rx="3"/>
      <circle cx="549" cy="770" r="5"/>
      <line x1="559" y1="768" x2="571" y2="768"/>
      <line x1="559" y1="777" x2="571" y2="777"/>
    </g>
    <text class="rate-heading" x="619" y="787">Membership Rates:</text>
    <g fill="var(--red)">
      <circle cx="605" cy="836" r="7"/><circle cx="605" cy="872" r="7"/>
    </g>
    <text class="rate-item" x="619" y="846">$99/Month</text>
    <text class="rate-item" x="619" y="882">$49 Heroes Rate</text>

    <g class="rate-icon" fill="none" stroke="var(--icon)" stroke-width="3">
      <circle cx="545" cy="925" r="6"/><circle cx="557" cy="920" r="6"/><circle cx="569" cy="925" r="6"/>
      <path d="M535 948 q10 -16 20 0 M547 943 q10 -16 20 0 M559 948 q10 -16 20 0"/>
    </g>
    <text class="rate-heading" x="619" y="949">Family Plan:</text>
    <g fill="var(--red)">
      <circle cx="605" cy="997" r="7"/><circle cx="605" cy="1034" r="7"/><circle cx="605" cy="1071" r="7"/>
    </g>
    <text class="rate-item" x="619" y="1007">2 People $149</text>
    <text class="rate-item" x="619" y="1044">3 People $199</text>
    <text class="rate-item" x="619" y="1081">4 People $299</text>

    <g class="rate-icon" fill="none" stroke="var(--icon)" stroke-width="3">
      <line x1="535" y1="1128" x2="579" y2="1128"/>
      <rect x="531" y="1120" width="6" height="16"/><rect x="577" y="1120" width="6" height="16"/>
      <circle cx="557" cy="1138" r="5"/>
      <path d="M557 1143 v12 M549 1160 l8 -6 l8 6"/>
    </g>
    <text class="rate-heading" x="619" y="1150">Personal Training Rates:</text>
    <g fill="var(--red)">
      <circle cx="605" cy="1198" r="7"/><circle cx="605" cy="1235" r="7"/><circle cx="605" cy="1271" r="7"/>
      <circle cx="605" cy="1308" r="7"/><circle cx="605" cy="1345" r="7"/>
    </g>
    <text class="rate-item" x="619" y="1208">1 session $102</text>
    <text class="rate-item" x="619" y="1245">5 sessions $490</text>
    <text class="rate-item" x="619" y="1281">10 sessions $940</text>
    <text class="rate-item" x="619" y="1318">20 sessions $1,800</text>
    <text class="rate-item" x="619" y="1355">40 sessions $3,400</text>
  </g>

  <polygon class="contact-band" points="0,1294 233,1223 459,1396 1100,1396 1100,1540 0,1540" fill="var(--red)"/>
  <polygon class="contact-band-corner" points="0,1484 0,1540 90,1540" fill="var(--white)"/>

  <g class="pin-icon" fill="none" stroke="var(--white)" stroke-width="3">
    <path d="M233 1342 c-14 -16 -18 -22 -18 -30 a18 18 0 0 1 36 0 c0 8 -4 14 -18 30z"/>
    <circle cx="233" cy="1312" r="6"/>
  </g>
  <text class="address" x="233" y="1387" text-anchor="middle">2817 Larkmoor Commerce Dr.</text>
  <text class="address" x="233" y="1424" text-anchor="middle">Suite 214 Harlow, OH 43215</text>
  <g class="globe-icon" fill="none" stroke="var(--white)" stroke-width="2.5">
    <circle cx="233" cy="1458" r="12"/>
    <ellipse cx="233" cy="1458" rx="5" ry="12"/>
    <line x1="221" y1="1458" x2="245" y2="1458"/>
  </g>
  <text class="address" x="233" y="1503" text-anchor="middle">www.vantagesh-example.com</text>

  <g class="phone-icon">
    <circle cx="505" cy="1468" r="34" fill="none" stroke="var(--white)" stroke-width="5"/>
    <path d="M492 1450 l8 -3 l6 12 l-5 4 q4 10 13 14 l4 -5 l12 6 l-3 8 q-22 2 -35 -36z" fill="var(--white)"/>
  </g>
  <text class="phone-number" x="561" y="1491">614-555-0187</text>
</svg>
</div>
</body>
</html>
```